Business Card Design Project

I need a new business card design for my building/development company: Kestrel Ridge Builders.

We specialise in small sub-divisions, multi-story developments and new house builds.
We handle the whole process from concept stage right throught to a fully developed property.
Updates

Target Market(s)

people looking to develop their property and need help. New property buyers

Industry/Entity Type

House

Requirements
Must have
• My logo on both sides:
Side 1: Logo taking up whole side as per old card but with a color/style change.

Side 2: Contact page: include logo but the rest just surprise me!

All contact details will be: (and need to be changable for each employee) I'll inform you of specifics before printing.

Name Surname
Position ie. Managing director
M: insert mobile
E: insert email
P.O. Box 518, Ashwell, Vic, 3094
www.kestrelridgebuilders.com.au

Nice to have
• Colors i'd like: (not necessarily all but this is the basic idea)

Black, blue, grey, silver, white

```html
<!DOCTYPE html>
<html lang="en">
<head>
<meta charset="utf-8">
<title>Kestrel Ridge Builders – Business Card</title>
<link href="https://fonts.googleapis.com/css2?family=Arimo:wght@400;700&family=Open+Sans:wght@400&display=swap" rel="stylesheet">
<style>
  :root {
    --page-bg: #ecebe8;
    --card-black: #000000;
    --card-white: #ffffff;
    --brand-blue: #1a8fd6;
    --text-dark: #1b1b1b;
    --text-light: #ffffff;
    --pattern-light: #2c2c2c;
    --pattern-dark: #0b0b0b;
  }
  * { margin: 0; padding: 0; box-sizing: border-box; }
  html, body {
    width: 943px;
    height: 1200px;
    overflow: hidden;
    background: var(--page-bg);
    font-family: "Arimo", Arial, sans-serif;
  }
  .canvas {
    position: relative;
    width: 943px;
    height: 1200px;
  }
  .card {
    position: absolute;
    left: 93px;
    width: 770px;
    height: 383px;
    box-shadow: 4px 6px 14px rgba(0, 0, 0, 0.28);
    overflow: hidden;
  }

  /* Front side */
  .card-front {
    top: 174px;
    background: var(--card-black);
  }
  .front-texture {
    position: absolute;
    inset: 0;
    background: radial-gradient(ellipse at center, var(--pattern-light) 0%, var(--pattern-dark) 85%);
  }
  .front-mark {
    position: absolute;
    left: 317px;
    top: 56px;
    width: 136px;
    height: 136px;
    background: var(--brand-blue);
  }
  .front-brand {
    position: absolute;
    left: 0;
    right: 0;
    top: 254px;
    text-align: center;
    color: var(--text-light);
  }
  .front-name {
    font-weight: 700;
    font-size: 50px;
    line-height: 1;
    letter-spacing: -0.5px;
  }
  .front-tagline {
    margin-top: 8px;
    font-family: "Open Sans", Verdana, sans-serif;
    font-size: 23px;
    letter-spacing: 0.5px;
  }

  /* Back side */
  .card-back {
    top: 665px;
    background: var(--card-white);
  }
  .back-mark {
    position: absolute;
    left: 560px;
    top: 34px;
    width: 96px;
    height: 96px;
    background: var(--brand-blue);
  }
  .back-brand {
    position: absolute;
    right: 24px;
    top: 138px;
    font-weight: 700;
    font-size: 27px;
    color: var(--text-dark);
    letter-spacing: -0.3px;
  }
  .person {
    position: absolute;
    left: 42px;
    top: 135px;
  }
  .person-name {
    font-weight: 700;
    font-size: 25px;
    color: var(--brand-blue);
  }
  .person-role {
    margin-top: 6px;
    font-size: 20px;
    color: var(--text-dark);
  }
  .contact-panel {
    position: absolute;
    left: 0;
    top: 213px;
    width: 418px;
    height: 103px;
    background: var(--brand-blue);
    border-radius: 0 9px 9px 0;
    padding: 11px 0 0 42px;
    color: var(--text-light);
    font-size: 20px;
    line-height: 29px;
  }
  .contact-panel b { font-weight: 700; }
  .website {
    position: absolute;
    left: 0;
    right: 0;
    top: 330px;
    text-align: center;
    font-size: 26px;
    color: var(--text-dark);
  }
  .base-band {
    position: absolute;
    left: 0;
    right: 0;
    bottom: 0;
    height: 15px;
    background: var(--brand-blue);
  }
</style>
</head>
<body>
  <main class="canvas">
    <section class="card card-front">
      <div class="front-texture" role="img" aria-label="Dark repeating house-shape pattern background"></div>
      <div class="front-mark"></div>
      <div class="front-brand">
        <div class="front-name">Kestrel Ridge Builders</div>
        <div class="front-tagline">renovation-construction-development</div>
      </div>
    </section>

    <section class="card card-back">
      <div class="back-mark"></div>
      <div class="back-brand">Kestrel Ridge Builders</div>
      <div class="person">
        <div class="person-name">Marcus Doyle</div>
        <div class="person-role">Director</div>
      </div>
      <div class="contact-panel">
        <div><b>M</b>: 0418552 907</div>
        <div><b>E</b>: marcus@kestrelridgebuilders.com.au</div>
        <div>P.O. Box 518, Ashwell, Vic, 3094</div>
      </div>
      <div class="website">www.kestrelridgebuilders.com.au</div>
      <div class="base-band"></div>
    </section>
  </main>
</body>
</html>
```